Re-Design an adult education portal

I need support to re-design an adult education portal. Currently the customer has an incomplete website which should be prepared in a new format.
I have the idea how to realize, but I have no clue how to design it. The hard thing is to have a "beautiful" website with available logo and main color. I hope you can support me.

Name of Website: tovrenu (tovrenu.ch)
Content: adult eduction for adult in safety at work, mountain climbing, dog school. various courses in different areas. But on old webpage is hard to find the different possibilities.
main color: Ral 6011 (green) -> #6C7C59
logo: you see on top of website the logo (2 dogs and a mountain with a colour gradient).

new website: for new webpage I decided to have a navigation for each section of education. In the main area I would like to have some pictures to give an idea what content is behind. At the moment it looks terrible, so I decided to use you as support for me to make the webpage prettier :). And maybe you have an better idea how to make it great. -> current state of new web page: https://tovrenu.bask-om.ch/

Target Market(s)

adult eduction for adult in safety at work, mountain climbing, dog school

Number of Pages Required

1 page

Font styles to use
Serif
Sans Serif

Requirements
Must have
• As main color is set "Ral 6011" (green) -> #6C7C59

```html
<!DOCTYPE html>
<html lang="de">
<head>
<meta charset="utf-8">
<title>tovrenu – Ausbildungs- und Kurspartner</title>
<link rel="stylesheet" href="https://fonts.googleapis.com/css2?family=Outfit:wght@200;300;400;500;600&family=Nunito+Sans:wght@400;600;700&display=swap">
<style>
:root{
  --green:#6c7c59;
  --green-dark:#56654a;
  --ink:#222;
  --text:#555;
  --link:#2a3a8c;
  --soft:#f7f7f7;
  --line:#e4e4e4;
  --white:#fff;
  --star:#f4b400;
}
*{box-sizing:border-box;margin:0;padding:0}
html,body{width:1200px;height:3125px;overflow:hidden}
body{position:relative;background:var(--white);font-family:"Nunito Sans",sans-serif;color:var(--text)}
.abs{position:absolute}
a{color:inherit;text-decoration:none}

/* header */
.site-header{position:absolute;left:0;top:0;width:1200px;height:53px;background:var(--white);z-index:3}
.brand{position:absolute;left:32px;top:18px;width:139px;height:73px;background:var(--white);border:1px solid #ddd;display:flex;align-items:center;justify-content:center;font-family:"Outfit",sans-serif;font-size:26px;font-weight:400;color:var(--green);z-index:4}
.nav-item{position:absolute;top:18px;font-size:12px;color:#444}
.nav-item svg{margin-left:3px;vertical-align:middle}
.call{position:absolute;left:1044px;top:10px}
.call-label{font-size:11px;letter-spacing:2.5px;color:var(--green);display:flex;align-items:center;gap:6px}
.call-icon{width:18px;height:18px;border-radius:50%;background:var(--green);display:inline-flex;align-items:center;justify-content:center}
.call-number{font-family:"Outfit",sans-serif;font-weight:600;font-size:15px;color:var(--green);margin-top:1px;margin-left:4px}

/* hero */
.hero{position:absolute;left:0;top:53px;width:1200px;height:594px;background:linear-gradient(90deg,#6e7f56 0%,#72865a 30%,#7a8c5c 45%,#8a9468 60%,#5f6f44 80%,#3e4e2c 100%)}
.hero h1{position:absolute;left:160px;top:176px;font-family:"Outfit",sans-serif;font-weight:200;font-size:49px;line-height:43px;color:var(--white)}
.hero p{position:absolute;left:165px;top:278px;width:330px;font-size:16px;line-height:22px;color:var(--white)}
.btn-hero{position:absolute;left:162px;top:356px;width:159px;height:40px;background:var(--white);color:var(--green);font-size:13px;letter-spacing:.6px;display:flex;align-items:center;justify-content:center;gap:12px}

/* courses */
.courses{position:absolute;left:0;top:647px;width:1200px;height:716px;background:var(--soft)}
.section-title{position:absolute;left:0;width:1200px;text-align:center;font-family:"Outfit",sans-serif;font-weight:600;color:var(--green)}
.course{position:absolute;width:292px;height:260px}
.course.active{background:var(--white);box-shadow:0 4px 18px rgba(0,0,0,.08)}
.course.active::after{content:"";position:absolute;left:0;right:10px;bottom:12px;height:4px;background:var(--green)}
.course-icon{position:absolute;left:22px;top:68px;width:46px;height:46px;border:2px solid #555;border-radius:6px;background:#ececec}
.course h3{position:absolute;left:22px;top:133px;font-family:"Outfit",sans-serif;font-weight:500;font-size:19px;color:var(--ink)}
.course p{position:absolute;left:22px;top:166px;font-size:11px;line-height:22px;color:#444;width:230px}
.more{font-size:10px;font-weight:700;color:var(--link);display:inline-flex;align-items:center;gap:6px}
.course .more{position:absolute;left:22px}
.divider-v{position:absolute;width:1px;background:var(--line)}
.divider-h{position:absolute;height:1px;background:var(--line)}
.dot-btn{position:absolute;width:24px;height:24px;border-radius:50%;background:#ddd;display:flex;align-items:center;justify-content:center}

/* about */
.about-title{position:absolute;left:164px;top:1412px;font-family:"Outfit",sans-serif;font-weight:600;font-size:37px;color:var(--green)}
.about-text{position:absolute;left:164px;top:1471px;width:410px;font-size:12.5px;line-height:30px;color:#555}
.photo{position:absolute}
.frame-l{position:absolute;left:943px;top:1691px;width:94px;height:99px;border-right:17px solid var(--green);border-bottom:17px solid var(--green)}

/* testimonials */
.reviews{position:absolute;left:0;top:1872px;width:1200px;height:357px;background:var(--soft)}
.review{position:absolute;width:299px;height:170px;background:var(--white);box-shadow:0 3px 14px rgba(0,0,0,.06)}
.review h4{position:absolute;left:51px;top:18px;font-family:"Outfit",sans-serif;font-weight:500;font-size:15px;color:var(--ink)}
.review .stars{position:absolute;left:51px;top:40px}
.review p{position:absolute;left:51px;top:62px;width:235px;font-size:10.5px;line-height:20px;color:#444}
.avatar-ring{position:absolute;width:74px;height:74px;border-radius:50%;border:1px solid #e6e6e6;background:var(--white)}
.avatar{position:absolute;left:6px;top:6px;width:60px;height:60px;border-radius:50%;background:radial-gradient(circle at 50% 40%,#eae6e2,#c8c2bc)}

/* schedule */
.col{position:absolute;background:var(--soft);border-radius:8px}
.col.lifted{background:var(--soft);box-shadow:0 4px 20px rgba(0,0,0,.09)}
.col h3{position:absolute;left:0;width:100%;text-align:center;font-family:"Outfit",sans-serif;font-weight:500;color:var(--ink)}
.row{position:absolute;font-size:11px;line-height:17px;color:#444;display:flex;gap:8px}
.row svg{flex:none;margin-top:4px}

/* footer */
.site-footer{position:absolute;left:0;top:2788px;width:1200px;height:337px;background:var(--green-dark);color:var(--white)}
.foot-brand{position:absolute;left:164px;top:73px;width:178px;height:95px;background:var(--white);display:flex;align-items:center;justify-content:center;font-family:"Outfit",sans-serif;font-size:30px;color:var(--green)}
.foot-col{position:absolute;top:52px;font-size:11px}
.foot-col h5{font-size:12px;font-weight:700;margin-bottom:6px}
.foot-col li{list-style:none;line-height:28px}
.foot-col .block{margin-bottom:20px;line-height:16px}
.foot-rule{position:absolute;left:164px;top:290px;width:873px;height:1px;background:rgba(255,255,255,.15)}
</style>
</head>
<body>

<header class="site-header">
  <span class="nav-item" style="left:407px">Arbeitssicherheit<svg width="8" height="5"><path d="M1 1l3 3 3-3" fill="none" stroke="#999"/></svg></span>
  <span class="nav-item" style="left:545px">Erste Hilfe<svg width="8" height="5"><path d="M1 1l3 3 3-3" fill="none" stroke="#999"/></svg></span>
  <span class="nav-item" style="left:645px">Hundeschule<svg width="8" height="5"><path d="M1 1l3 3 3-3" fill="none" stroke="#999"/></svg></span>
  <span class="nav-item" style="left:763px">CZV<svg width="8" height="5"><path d="M1 1l3 3 3-3" fill="none" stroke="#999"/></svg></span>
  <span class="nav-item" style="left:832px">Bergausbildung<svg width="8" height="5"><path d="M1 1l3 3 3-3" fill="none" stroke="#999"/></svg></span>
  <span class="nav-item" style="left:966px">tovrenu<svg width="8" height="5"><path d="M1 1l3 3 3-3" fill="none" stroke="#999"/></svg></span>
  <div class="call">
    <div class="call-label"><span class="call-icon"><svg width="10" height="10" viewBox="0 0 24 24"><path d="M6.6 10.8a15 15 0 0 0 6.6 6.6l2.2-2.2c.3-.3.7-.4 1-.2 1.1.4 2.3.6 3.6.6.6 0 1 .4 1 1V20c0 .6-.4 1-1 1A17 17 0 0 1 3 4c0-.6.4-1 1-1h3.5c.6 0 1 .4 1 1 0 1.3.2 2.5.6 3.6.1.3 0 .7-.2 1z" fill="#fff"/></svg></span>jetzt anrufen</div>
    <div class="call-number">+41 79 512 48 30</div>
  </div>
</header>
<div class="brand">tovrenu.ch</div>

<section class="hero" role="img" aria-label="Photo: two course leaders sitting in a green meadow with their two dogs">
  <h1>Ihr Ausbildungs-<br>und Kurspartner</h1>
  <p>Wir bieten Ihnen Wünschen entsprechende Ausbildungen, zielorientiert und Ihrem Können und Wissen angepasst.</p>
  <a class="btn-hero" href="#">WEITERLESEN <svg width="11" height="10" viewBox="0 0 11 10"><path d="M0 5h9M6 1.5L9.5 5 6 8.5" fill="none" stroke="#6c7c59" stroke-width="1.4"/></svg></a>
</section>

<section class="courses">
  <h2 class="section-title" style="top:65px;font-size:36px">Hubarbeitsbühnen Kurs</h2>

  <div class="divider-v" style="left:443px;top:154px;height:152px"></div>
  <div class="divider-v" style="left:752px;top:154px;height:152px"></div>
  <div class="divider-h" style="left:443px;top:415px;width:596px"></div>
  <div class="divider-h" style="left:161px;top:415px;width:282px"></div>
  <div class="divider-v" style="left:443px;top:415px;height:245px"></div>
  <div class="divider-v" style="left:752px;top:415px;height:245px"></div>

  <article class="course active" style="left:162px;top:155px">
    <div class="course-icon" role="img" aria-label="Forklift icon"></div>
    <h3>Staplerkurse</h3>
    <p>Grundausbildung</p>
    <a class="more" href="#" style="top:190px">Weiterlesen <svg width="9" height="8"><path d="M0 4h7M4.5 1L7.5 4 4.5 7" fill="none" stroke="#2a3a8c" stroke-width="1.3"/></svg></a>
  </article>
  <article class="course" style="left:468px;top:155px">
    <div class="course-icon" role="img" aria-label="Safety helmet icon"></div>
    <h3>PSAgA</h3>
    <p>Persönliche Schutzausrüstung<br>gegen Absturz (PSAgA)</p>
    <a class="more" href="#" style="top:214px">Weiterlesen <svg width="9" height="8"><path d="M0 4h7M4.5 1L7.5 4 4.5 7" fill="none" stroke="#2a3a8c" stroke-width="1.3"/></svg></a>
  </article>
  <article class="course" style="left:779px;top:155px">
    <div class="course-icon" role="img" aria-label="Aerial work platform icon"></div>
    <h3>Hubarbeitsbühne</h3>
    <p>Bedienerschulung<br>Bedienerschulung / CZV</p>
    <a class="more" href="#" style="top:214px">Weiterlesen <svg width="9" height="8"><path d="M0 4h7M4.5 1L7.5 4 4.5 7" fill="none" stroke="#2a3a8c" stroke-width="1.3"/></svg></a>
  </article>

  <article class="course" style="left:160px;top:428px">
    <div class="course-icon" role="img" aria-label="Dog training icon"></div>
    <h3>Hundeschule</h3>
    <p style="line-height:18px;top:170px">Welpenförderung<br>Agilty Mantrailing</p>
    <a class="more" href="#" style="top:212px">Weiterlesen <svg width="9" height="8"><path d="M0 4h7M4.5 1L7.5 4 4.5 7" fill="none" stroke="#2a3a8c" stroke-width="1.3"/></svg></a>
  </article>
  <article class="course" style="left:468px;top:428px">
    <div class="course-icon" role="img" aria-label="First aid kit icon"></div>
    <h3>Nothelfer</h3>
    <p style="line-height:18px;top:170px">Auffrischungskurs Gutschein für<br>Fahrstunden bei xyz</p>
    <a class="more" href="#" style="top:212px">Weiterlesen <svg width="9" height="8"><path d="M0 4h7M4.5 1L7.5 4 4.5 7" fill="none" stroke="#2a3a8c" stroke-width="1.3"/></svg></a>
  </article>
  <article class="course" style="left:777px;top:428px">
    <div class="course-icon" role="img" aria-label="Paramedic icon"></div>
    <h3>Sanitätsschulung</h3>
    <p style="line-height:18px;top:170px">Auffrischungskurs</p>
    <a class="more" href="#" style="top:212px">Weiterlesen <svg width="9" height="8"><path d="M0 4h7M4.5 1L7.5 4 4.5 7" fill="none" stroke="#2a3a8c" stroke-width="1.3"/></svg></a>
  </article>

  <span class="dot-btn" style="left:981px;top:648px"><svg width="6" height="9"><path d="M5 1L1.5 4.5 5 8" fill="none" stroke="#fff" stroke-width="1.4"/></svg></span>
  <span class="dot-btn" style="left:1013px;top:648px"><svg width="6" height="9"><path d="M1 1l3.5 3.5L1 8" fill="none" stroke="#fff" stroke-width="1.4"/></svg></span>
</section>

<section class="about">
  <h2 class="about-title">Über Uns</h2>
  <p class="about-text">In meiner Beruflichen Laufbahn erlebte ich immer wieder Situationen, welche in mir die Idee reifen liessen, jedem interessierten Menschen ein Grundwissen zukommen zu lassen, welches ihn bei einer Notsituation richtig und mit der nötigen Ruhe reagieren lässt. Das Zusammenlegen &amp; Kombinieren von Wissen und Fertigkeiten der verschiedenen Fachbereiche gibt dem Menschen Sicherheit und Vertrauen in seinem Handeln. Aus eigener Erfahrung hat sich gezeigt: je professioneller man auf Grenzsituationen vorbereitet ist, desto sicherer und erfolgreicher kann eine Notfallsituation gemeistert und sogar Leben gerettet werden.</p>
  <a class="more abs" href="#" style="left:164px;top:1786px">Weiterlesen <svg width="9" height="8"><path d="M0 4h7M4.5 1L7.5 4 4.5 7" fill="none" stroke="#2a3a8c" stroke-width="1.3"/></svg></a>

  <div class="frame-l"></div>
  <div class="photo" style="left:664px;top:1456px;width:142px;height:295px;background:linear-gradient(180deg,#3f64a8,#5a5446 55%,#8b8478)" role="img" aria-label="Photo: dog among autumn trees on rocks"></div>
  <div class="photo" style="left:812px;top:1491px;width:115px;height:198px;background:linear-gradient(180deg,#4c6ea8,#6a5a44 60%,#3a3028)" role="img" aria-label="Photo: man with dog under trees"></div>
  <div class="photo" style="left:812px;top:1694px;width:115px;height:105px;background:linear-gradient(180deg,#7a6a52,#9a9488)" role="img" aria-label="Photo: dog resting on rocks"></div>
  <div class="photo" style="left:933px;top:1532px;width:79px;height:231px;background:linear-gradient(180deg,#4a6ba6,#5b4a3a 55%,#8a8278)" role="img" aria-label="Photo: woman in the autumn forest"></div>
</section>

<section class="reviews">
  <h2 class="section-title" style="top:58px;font-size:41px">Unsere Zeugnisse</h2>
  <svg class="abs" style="left:188px;top:187px" width="12" height="24"><path d="M10 1L2 12l8 11" fill="none" stroke="#bbb" stroke-width="1.5"/></svg>
  <svg class="abs" style="left:999px;top:168px" width="12" height="24"><path d="M2 1l8 11-8 11" fill="none" stroke="#bbb" stroke-width="1.5"/></svg>

  <article class="review" style="left:277px;top:130px">
    <h4>Vel Illum</h4>
    <svg class="stars" width="70" height="12" viewBox="0 0 70 12"><g fill="#f4b400"><path id="st" d="M6 0l1.8 3.8 4.2.5-3.1 2.9.8 4.1L6 9.3 2.3 11.3l.8-4.1L0 4.3l4.2-.5z"/><use href="#st" x="14"/><use href="#st" x="28"/><use href="#st" x="42"/><use href="#st" x="56"/></g></svg>
    <p>vel illum dolore eu feugiat nulla facilisis at vero eros et accumsan et iusto odio dignissim qui blandit praesent luptatum zzril delenit augue duis dolore te it nulla facilisis.</p>
  </article>
  <div class="avatar-ring" style="left:236px;top:146px"><div class="avatar" role="img" aria-label="Portrait photo of reviewer"></div></div>

  <article class="review" style="left:666px;top:130px">
    <h4>Dolore Te</h4>
    <svg class="stars" width="70" height="12" viewBox="0 0 70 12"><g fill="#f4b400"><use href="#st"/><use href="#st" x="14"/><use href="#st" x="28"/><use href="#st" x="42"/><use href="#st" x="56"/></g></svg>
    <p>Ut wisi enim ad minim veniam, quis nostrud exerci tation ullamcorper suscipit lobortis nisl ut aliquip ex ea ullamcorper suscipit lobortis nisl ut aliquip ex ea</p>
  </article>
  <div class="avatar-ring" style="left:625px;top:146px"><div class="avatar" role="img" aria-label="Portrait photo of reviewer"></div></div>
</section>

<section class="schedule">
  <h2 class="section-title" style="top:2292px;font-size:43px">Termine</h2>
  <svg width="0" height="0" style="position:absolute"><defs><path id="tick" d="M1 4l2.5 2.5L8 1.5" fill="none" stroke="#6c7c59" stroke-width="1.6"/></defs></svg>

  <div class="col" style="left:147px;top:2402px;width:168px;height:311px">
    <h3 style="top:40px;font-size:19px">Kursnummer</h3>
    <div class="row" style="left:60px;top:87px"><svg width="9" height="8"><use href="#tick"/></svg>21011</div>
    <div class="row" style="left:60px;top:130px"><svg width="9" height="8"><use href="#tick"/></svg>21012</div>
    <div class="row" style="left:60px;top:172px"><svg width="9" height="8"><use href="#tick"/></svg>21021</div>
    <div class="row" style="left:60px;top:215px"><svg width="9" height="8"><use href="#tick"/></svg>21022</div>
    <div class="row" style="left:60px;top:256px"><svg width="9" height="8"><use href="#tick"/></svg>21022</div>
  </div>

  <div class="col lifted" style="left:322px;top:2374px;width:200px;height:366px">
    <h3 style="top:24px;font-size:31px">Ort</h3>
    <div class="row" style="left:79px;top:94px"><svg width="9" height="8"><use href="#tick"/></svg>Steg</div>
    <div class="row" style="left:79px;top:141px"><svg width="9" height="8"><use href="#tick"/></svg>Steg</div>
    <div class="row" style="left:79px;top:189px"><svg width="9" height="8"><use href="#tick"/></svg>Steg</div>
    <div class="row" style="left:79px;top:236px"><svg width="9" height="8"><use href="#tick"/></svg>Steg</div>
    <div class="row" style="left:79px;top:283px"><svg width="9" height="8"><use href="#tick"/></svg>Steg</div>
  </div>

  <div class="col" style="left:528px;top:2402px;width:170px;height:311px">
    <h3 style="top:22px;font-size:19px">Datum</h3>
    <div class="row" style="left:46px;top:66px"><svg width="9" height="8"><use href="#tick"/></svg>25.01.2021</div>
    <div class="row" style="left:46px;top:108px"><svg width="9" height="8"><use href="#tick"/></svg>29.01.2021</div>
    <div class="row" style="left:46px;top:151px"><svg width="9" height="8"><use href="#tick"/></svg>9.02.2021</div>
    <div class="row" style="left:46px;top:193px"><svg width="9" height="8"><use href="#tick"/></svg>15.02.2021</div>
    <div class="row" style="left:46px;top:236px"><svg width="9" height="8"><use href="#tick"/></svg>16.02.2021</div>
  </div>

  <div class="col" style="left:705px;top:2402px;width:170px;height:311px">
    <h3 style="top:22px;font-size:19px">Kurs</h3>
    <div class="row" style="left:16px;top:66px"><svg width="9" height="8"><use href="#tick"/></svg>Hubarbeitsbühnen<br>Bedienerschulung</div>
    <div class="row" style="left:16px;top:108px"><svg width="9" height="8"><use href="#tick"/></svg>Hubarbeitsbühnen<br>Bedienerschulung / CZV</div>
    <div class="row" style="left:16px;top:151px"><svg width="9" height="8"><use href="#tick"/></svg>PSA g A<br>Grundkurs / CZV</div>
    <div class="row" style="left:16px;top:193px"><svg width="9" height="8"><use href="#tick"/></svg>Hubarbeitsbühnen<br>Bedienerschulung</div>
    <div class="row" style="left:16px;top:236px"><svg width="9" height="8"><use href="#tick"/></svg>PSA g A<br>Grundkurs</div>
  </div>

  <div class="col" style="left:882px;top:2402px;width:170px;height:311px">
    <h3 style="top:22px;font-size:19px">Freie Plätze</h3>
    <div class="row" style="left:42px;top:66px"><svg width="9" height="8"><use href="#tick"/></svg>3</div>
    <div class="row" style="left:42px;top:108px"><svg width="9" height="8"><use href="#tick"/></svg>ausgebucht</div>
    <div class="row" style="left:42px;top:151px"><svg width="9" height="8"><use href="#tick"/></svg>ausgebucht</div>
    <div class="row" style="left:42px;top:193px"><svg width="9" height="8"><use href="#tick"/></svg>2</div>
    <div class="row" style="left:42px;top:236px"><svg width="9" height="8"><use href="#tick"/></svg>4</div>
  </div>
</section>

<footer class="site-footer">
  <div class="foot-brand">tovrenu.ch</div>
  <div class="foot-col" style="left:380px">
    <h5>links</h5>
    <ul><li>Arbeitssicherheit</li><li>Erste Hilfe</li><li>Hundeschule</li><li>CZV</li><li>Bergausbildung</li><li>tovrenu</li></ul>
  </div>
  <div class="foot-col" style="left:601px">
    <h5>Kurse</h5>
    <ul><li>Staplerkurse</li><li>PSAgA</li><li>Hubarbeitsbühne</li><li>Nothelfer</li><li>Sanitätsschulung</li><li>BLS AGD</li><li>Bergausbildung</li></ul>
  </div>
  <div class="foot-col" style="left:827px">
    <h5>Adresse</h5>
    <div class="block">Talweg 27<br>3905 Ortsel</div>
    <h5>Telefon</h5>
    <div class="block">+41 79 512 48 30</div>
    <h5>E-Mail</h5>
    <div class="block">info@tovrenu.ch</div>
  </div>
  <div class="foot-rule"></div>
</footer>

</body>
</html>
```